QM Studios needs and Interior Design Business card

I can do anything from Commercial to Residential and Free lance. Beginning to end in design selection process.
Need something to catch the eye of potential customers and vendors. From furniture to Tile and Cabinet selections. I can do it all.

Industry/Entity Type

Design Agency

Contact Information for Business Card

QM Studios- Design Consultanting Residential, Commerical
Maybe a cool detail background. Wall paper print that can have some texture

Font styles to use
Serif

Colors
709dcb
34a6d7
b868aa
e667a6
f59296
85acd3
ffffff
000000
5c5c5c

Requirements
Must have
• Square or Rectangular with Rounded edges
• Name
• Address
• Phone
• Email
Nice to have
• Some colored edges More simples not too busy
• Pattern detail in background.
Should not have
• Not too much color

```html
<!DOCTYPE html>
<html lang="en">
<head>
<meta charset="utf-8">
<title>QM Studios – Business Card</title>
<link href="https://fonts.googleapis.com/css2?family=Lato:wght@400&family=Raleway:wght@400&display=swap" rel="stylesheet">
<style>
  :root {
    --page-bg: #f4f4f4;
    --plum: #5a2a4e;
    --plum-light: #6e3862;
    --plum-dark: #4a2040;
    --silver: #dfe1e6;
    --silver-light: #eceef2;
    --ink: #2e2e2e;
    --frame: #5c5c5c;
    --mark: #c9c0cc;
  }
  * { box-sizing: border-box; margin: 0; padding: 0; }
  html, body { width: 1200px; height: 903px; overflow: hidden; }
  body { background: var(--page-bg); position: relative; }

  .card {
    position: absolute;
    left: 160px; top: 176px;
    width: 880px; height: 550px;
    border-radius: 20px;
    overflow: hidden;
    box-shadow: 0 6px 24px rgba(0,0,0,.18);
  }
  .card__brand {
    position: absolute; left: 0; top: 0;
    width: 100%; height: 320px;
    background: linear-gradient(135deg, var(--plum-light), var(--plum) 50%, var(--plum-dark));
  }
  .brand__emblem {
    position: absolute; left: 364px; top: 40px;
    width: 152px; height: 152px;
    border: 4px solid var(--mark);
    border-radius: 50%;
  }
  .brand__name {
    position: absolute; left: 0; top: 208px; width: 100%;
    text-align: center;
    font-family: "Raleway", sans-serif;
    font-size: 44px; letter-spacing: 5px;
    color: var(--mark);
  }
  .card__contact {
    position: absolute; left: 0; top: 320px;
    width: 100%; height: 230px;
    background: linear-gradient(135deg, var(--silver-light), var(--silver));
  }
  .contact__box {
    position: absolute; top: 22px;
    width: 252px; height: 188px;
    border: 2px solid var(--frame);
    text-align: center;
    font-family: "Lato", sans-serif;
    font-size: 19px; line-height: 26px;
    color: var(--ink);
  }
  .contact__box--phone { left: 40px; }
  .contact__box--web { left: 314px; }
  .contact__box--place { left: 588px; }
  .contact__icon { display: block; margin: 16px auto 0; }
  .contact__rule {
    width: 90px; height: 2px; margin: 8px auto 18px;
    background: var(--frame);
  }
</style>
</head>
<body>
  <div class="card">
    <div class="card__brand" role="img" aria-label="Plum wallpaper-style triangle pattern background">
      <div class="brand__emblem"></div>
      <div class="brand__name">QM Studios</div>
    </div>
    <div class="card__contact">
      <div class="contact__box contact__box--phone">
        <svg class="contact__icon" width="64" height="64" viewBox="0 0 64 64" aria-hidden="true">
          <circle cx="32" cy="32" r="29" fill="none" stroke="#2e2e2e" stroke-width="3"/>
          <path d="M24 19c2 0 4 5 4 6s-3 2-3 4 6 9 9 10c2 0 3-3 4-3s6 2 6 4-3 5-6 5c-8 0-19-11-19-19 0-4 3-7 5-7z" fill="#2e2e2e"/>
        </svg>
        <div class="contact__rule"></div>
        <p>0044 0203 555 128</p>
        <p>0044 0203 555 412</p>
      </div>
      <div class="contact__box contact__box--web">
        <svg class="contact__icon" width="64" height="64" viewBox="0 0 64 64" aria-hidden="true">
          <circle cx="32" cy="32" r="29" fill="none" stroke="#2e2e2e" stroke-width="3"/>
          <circle cx="32" cy="32" r="15" fill="none" stroke="#2e2e2e" stroke-width="3"/>
          <ellipse cx="32" cy="32" rx="6" ry="15" fill="none" stroke="#2e2e2e" stroke-width="2"/>
          <line x1="17" y1="32" x2="47" y2="32" stroke="#2e2e2e" stroke-width="2"/>
        </svg>
        <div class="contact__rule"></div>
        <p>hello@qmstudios.com</p>
        <p>www.qmstudios.com</p>
      </div>
      <div class="contact__box contact__box--place">
        <svg class="contact__icon" width="64" height="64" viewBox="0 0 64 64" aria-hidden="true">
          <circle cx="32" cy="32" r="29" fill="none" stroke="#2e2e2e" stroke-width="3"/>
          <path d="M32 48c-6-8-11-13-11-20a11 11 0 0 1 22 0c0 7-5 12-11 20z" fill="none" stroke="#2e2e2e" stroke-width="3"/>
          <circle cx="32" cy="28" r="4" fill="#2e2e2e"/>
        </svg>
        <div class="contact__rule"></div>
        <p>24 Elm Row, Park St,</p>
        <p>Perth, Australia</p>
      </div>
    </div>
  </div>
</body>
</html>
```